Popcorn, ice cream, alcohol infused shakes shop

Create a clean simple website with pictures and bold type for a popcorn, ice cream and boozy shake shop. The site should have:
- Unique and Large Typography
- Large & Responsive Hero (stunning, elicits a response) Images.No concern with above or below the fold. Create a strong visual experience that encourages visitors to scroll down to read more. Use large images to visually tell a story without having to rely on just text.
- Flat image designs
- Place for me to upload an ad type video
- Hidden type menu (three line menu)
- A few small card like images (food, gift bags, tins, etc.) menu items with a brief description.

Target Market(s)

21-49 years of age for the boozy shakes. Soccer moms for sports teams & sleepovers, professionals (teachers, realtors, pharm sales), gifts for family and friends. Also some kids

Coding

Coded - Design and coding required

Number of Pages Required

5+ page

Font styles to use
Sans Serif

Colors

Designer to choose colors to be used in the design.

Requirements
Must have
• Images of gourmet popcorn, fancy shakes, ice cream, gift bags and popcorn tins. Holiday popcorn tins and gift bags along with grift certificates. Ability for visitors to send a contact form to rt@fizzlane.net
• Five pages - Home Page, AboutUs, Menu, Gift/Promotion, Contact Us
Nice to have
• Smooth flow on the home page. Mostly images and bold text.
Should not have
• Too many words. Boring text fonts

```html
<!DOCTYPE html>
<html lang="en">
<head>
<meta charset="utf-8">
<title>Fizz Lane – Home</title>
<link href="https://fonts.googleapis.com/css2?family=Montserrat:wght@400;600;700;800&family=Open+Sans:ital,wght@0,400;0,600;1,400&display=swap" rel="stylesheet">
<style>
:root{
  --stage:#a39fa0;
  --green:#8cc63f;
  --green-dark:#6fae25;
  --red:#e0202a;
  --red-soft:#e9707a;
  --ink:#222;
  --muted:#777;
  --light:#f1f1f3;
  --black:#000;
  --white:#fff;
}
*{box-sizing:border-box;margin:0;padding:0}
html,body{width:783px;height:1200px;overflow:hidden;background:var(--stage)}
body{position:relative;font-family:"Open Sans",sans-serif;color:var(--ink)}
.page{position:absolute;width:634px;height:2192px;background:var(--white);transform-origin:0 0;transform:scale(.504);overflow:hidden;box-shadow:0 0 12px rgba(0,0,0,.25)}
.page--home{left:46px;top:47px}
.page--popup{left:411px;top:47px}
.abs{position:absolute}
.topbar{left:0;top:0;width:634px;height:20px;background:var(--green);color:var(--white);font-size:7px;font-weight:600;display:flex;justify-content:space-between;align-items:center;padding:0 60px}
.header{left:0;top:20px;width:634px;height:56px;background:var(--white)}
.brand{left:58px;top:24px;font-family:"Montserrat",sans-serif;font-weight:800;font-size:18px;color:var(--red);line-height:20px;display:flex;align-items:center;gap:5px}
.brand i{display:block;width:12px;height:12px;border-radius:50%;background:var(--green)}
.search{left:248px;top:32px;width:164px;height:24px;border:1px solid #ddd;border-radius:12px;font-size:7px;color:#999;padding:6px 10px}
.search b{position:absolute;right:2px;top:2px;width:19px;height:19px;border-radius:50%;background:var(--red)}
.lang{left:428px;top:40px;font-size:7px}
.flag{left:451px;top:39px;width:16px;height:10px;background:linear-gradient(#c33 0 20%,#fff 20% 40%,#c33 40% 60%,#fff 60% 80%,#c33 80%);border:1px solid #ccc}
.social{left:478px;top:36px;display:flex;gap:4px}
.social span{width:15px;height:15px;border-radius:50%;background:#444}
.burger{left:564px;top:38px;width:10px}
.burger span{display:block;height:2px;background:#333;margin-bottom:2px}
.hero{left:0;top:76px;width:634px;height:300px;background:radial-gradient(circle at 70% 40%,#d9b48c,#efe7e3 45%,#f4eeee 70%)}
.hero-photo{left:250px;top:80px;width:330px;height:250px;border-radius:40%;background:radial-gradient(circle,#c08f5c,#d7b89a 55%,rgba(240,230,228,0) 72%)}
.hero-title{left:58px;top:172px;font-family:"Montserrat",sans-serif;font-weight:700;font-size:27px;color:var(--red)}
.hero-sub{left:60px;top:204px;font-family:"Montserrat",sans-serif;font-size:8.5px;font-weight:600;line-height:13px}
.hero-offer{left:58px;top:234px;font-family:"Montserrat",sans-serif;font-weight:700;font-size:13px;color:var(--red)}
.btn{display:inline-block;border-radius:12px;color:var(--white);font-family:"Montserrat",sans-serif;font-weight:700;font-size:7px;text-align:center;line-height:22px}
.btn--green{background:var(--green)}
.btn--red{background:var(--red)}
.dots{display:flex;flex-direction:column;gap:7px}
.dots span{width:6px;height:6px;border-radius:50%;border:1px solid #bbb}
.dots span:first-child{background:#fff;border-color:#fff}
.sec-icon{width:12px;height:14px}
.h2{font-family:"Montserrat",sans-serif;font-size:17px;font-weight:400;letter-spacing:.3px}
.h2 b{font-weight:700}
.para{font-size:6.8px;line-height:13.5px;color:var(--muted);text-align:justify}
.count{display:flex;gap:18px}
.count div{width:47px;height:47px;border-radius:50%;border:2px solid var(--green);text-align:center;font-family:"Montserrat",sans-serif;font-weight:700;font-size:12px;padding-top:8px;line-height:13px}
.count small{display:block;font-size:6px}
.photo{border:3px solid var(--white);box-shadow:0 0 3px rgba(0,0,0,.25)}
.menu-bg{left:0;top:636px;width:634px;height:364px;background:linear-gradient(180deg,#e8e6ea,#eceef1 50%,#e4e6ea)}
.card-img{width:139px;height:123px;background:var(--white);box-shadow:0 0 3px rgba(0,0,0,.12)}
.card-img div{position:absolute;inset:10px}
.card-title{width:139px;text-align:center;font-size:9px;font-weight:600}
.stars{color:#e9b300;font-size:6px;letter-spacing:-1px;text-align:center}
.card-text{width:150px;text-align:center;font-size:6px;line-height:13.5px;color:var(--muted)}
.sale{width:34px;height:34px;border-radius:50%;background:var(--red);color:var(--white);font-size:7.5px;font-weight:600;text-align:center;line-height:34px}
.recipe{left:0;top:1243px;width:634px;height:210px;background:linear-gradient(90deg,#e9707a,#e05c63 55%,#e43a3c)}
.recipe .h2,.recipe .para{color:var(--white)}
.arrow{font-size:22px;color:#222;font-weight:300}
.event-date{width:29px;height:32px;background:var(--green);color:var(--white);text-align:center;font-family:"Montserrat",sans-serif;font-weight:700;font-size:7px;line-height:9px;padding-top:3px}
.event-date b{display:block;font-size:14px;line-height:16px}
.event-title{font-family:"Montserrat",sans-serif;font-size:9.5px;line-height:13px}
.event-meta{font-size:6px}
.event-text{font-size:6px;line-height:12.5px;width:150px}
.footer{left:0;top:1900px;width:634px;height:292px}
.foot-h{font-family:"Montserrat",sans-serif;font-weight:700;font-size:7.5px;color:var(--white)}
.foot-t{font-size:7px;color:var(--white);line-height:13px}
.foot-ico{width:13px;height:13px;border:1px solid var(--green);border-radius:50%}
.foot-links{list-style:none}
.foot-links li{font-size:7px;color:var(--white);line-height:16.5px}
.foot-links li::before{content:"»";margin-right:10px}
.field{background:var(--white);font-size:6px;color:#999;padding:4px 8px}
.overlay{left:0;top:0;width:634px;height:2192px;background:rgba(214,214,214,.55)}
.modal{left:101px;top:113px;width:432px;height:236px;background:var(--white);text-align:center}
.modal-brand{left:0;top:18px;width:432px;font-family:"Montserrat",sans-serif;font-weight:800;font-size:20px;color:var(--red)}
.modal-h{left:40px;top:88px;width:352px;font-family:"Montserrat",sans-serif;font-weight:700;font-size:12px;line-height:13px;color:#444}
.modal-p{left:40px;top:124px;width:352px;font-size:10px;line-height:16px;color:#555}
.modal-input{left:50px;top:175px;width:330px;height:33px;border-radius:17px;background:#e8e8e8;font-size:7px;color:#777;text-align:left;padding:11px 16px}
.modal-btn{left:270px;top:177px;width:108px;height:29px;line-height:29px;border-radius:15px}
.close{left:516px;top:87px;width:40px;height:40px;border-radius:50%;background:var(--white);box-shadow:0 0 4px rgba(0,0,0,.3)}
</style>
</head>
<body>

<!-- ===== HOME PAGE ===== -->
<div class="page page--home">
  <div class="abs topbar"><span>☏ Call us Today : (555) 014-2290</span><span>✉ Email Address : hello@fizzlane.net</span></div>
  <div class="abs header"></div>
  <div class="abs brand"><i></i>FIZZ LANE</div>
  <div class="abs search">Search<b></b></div>
  <div class="abs lang">Eng ▾</div><div class="abs flag"></div>
  <div class="abs social"><span></span><span></span><span></span><span></span></div>
  <div class="abs burger"><span></span><span></span><span></span></div>

  <div class="abs hero"></div>
  <div class="abs hero-photo" role="img" aria-label="Two glass mugs of whipped-cream shake and caramel popcorn"></div>
  <div class="abs hero-title">FIZZ LANE</div>
  <div class="abs hero-sub">OREM IPSUM DOLOR SIT AMET,<br>CONSECTETUR ADIPISCING ELIT, SED DO</div>
  <div class="abs hero-offer">30% OFFER</div>
  <div class="abs btn btn--green" style="left:58px;top:262px;width:82px">GET STARTED</div>
  <div class="abs dots" style="left:603px;top:170px"><span></span><span></span><span></span><span></span><span></span></div>
  <svg class="abs" style="left:0;top:320px" width="634" height="70" viewBox="0 0 634 70"><path d="M0 60 Q300 -10 634 50 L634 70 L0 70Z" fill="#fff"/><path d="M150 22 Q420 0 634 50" fill="none" stroke="#6fae25" stroke-width="4"/></svg>

  <svg class="abs sec-icon" style="left:97px;top:412px" viewBox="0 0 12 14"><circle cx="6" cy="4" r="4" fill="#8cc63f"/><path d="M6 8V13M3 13H9" stroke="#999"/><circle cx="7" cy="1.5" r="1.5" fill="#e0202a"/></svg>
  <div class="abs h2" style="left:58px;top:436px">FEATURED <b>DISHES</b></div>
  <div class="abs para" style="left:59px;top:462px;width:242px">Lorem ipsum dolor sit amet, consectetur adipiscing elit, sed do eiusmod tempor incididunt ut labore et dolore magna aliqua. Ut enim ad minim veniam, quis nostrud exercitation ullamco laboris nisi ut aliquip ex ea commodo consequat. Duis aute irure dolor in reprehenderit in voluptate velit esse cillum dolore eu fugiat nulla pariatur. Excepteur sint occaecat cupidatat non proident,</div>
  <div class="abs count" style="left:58px;top:554px"><div>08<small>DAYS</small></div><div>20<small>HRS</small></div><div>10<small>MIN</small></div><div>45<small>SEC</small></div></div>
  <div class="abs photo" style="left:384px;top:422px;width:192px;height:160px;background:radial-gradient(circle,#e6e4e2,#bdbab7 60%,#efefef)" role="img" aria-label="Cookies and cream ice cream with chocolate cookies"></div>
  <div class="abs photo" style="left:332px;top:536px;width:92px;height:64px;background:linear-gradient(135deg,#8a6a4d,#d9d2c4 50%,#6d5441)" role="img" aria-label="Bowl of ice cream on a wooden table"></div>

  <div class="abs menu-bg"></div>
  <svg class="abs sec-icon" style="left:311px;top:670px" viewBox="0 0 12 14"><circle cx="6" cy="4" r="4" fill="#8cc63f"/><path d="M6 8V13M3 13H9" stroke="#999"/><circle cx="7" cy="1.5" r="1.5" fill="#e0202a"/></svg>
  <div class="abs h2" style="left:0;top:693px;width:634px;text-align:center">OUR <b style="font-weight:400">MENU</b></div>
  <div class="abs card-img" style="left:74px;top:729px"><div style="background:linear-gradient(180deg,#fff 30%,#c9d86b 60%,#b64d79)" role="img" aria-label="Colourful gourmet popcorn in a green cup"></div></div>
  <div class="abs card-img" style="left:246px;top:729px"><div style="background:radial-gradient(ellipse at 50% 45%,#8a5b3c,#d9c6b7 35%,#fff 60%)" role="img" aria-label="Ice cream sundae with a cherry"></div></div>
  <div class="abs card-img" style="left:418px;top:729px"><div style="background:radial-gradient(ellipse at 50% 45%,#8e1b25,#c46a70 35%,#fff 60%)" role="img" aria-label="Red boozy shake in a glass mug"></div></div>
  <div class="abs sale" style="left:195px;top:715px">Sale!</div>
  <div class="abs card-title" style="left:74px;top:861px">POPCORN</div>
  <div class="abs card-title" style="left:246px;top:861px">ICE CREAM</div>
  <div class="abs card-title" style="left:418px;top:861px">BOOZY SHAKE</div>
  <div class="abs stars" style="left:74px;top:874px;width:139px">★★★★★</div>
  <div class="abs stars" style="left:246px;top:874px;width:139px">★★★★★</div>
  <div class="abs stars" style="left:418px;top:874px;width:139px">★★★★★</div>
  <div class="abs card-text" style="left:69px;top:887px">Lorem ipsum dolor sit amet, consectetur adipiscing elit, sed do eiusmod tempor incididunt ut labore et dolore magna</div>
  <div class="abs card-text" style="left:241px;top:887px">Lorem ipsum dolor sit amet, consectetur adipiscing elit, sed do eiusmod tempor incididunt ut labore et dolore magna</div>
  <div class="abs card-text" style="left:413px;top:887px">Lorem ipsum dolor sit amet, consectetur adipiscing elit, sed do eiusmod tempor incididunt ut labore et dolore magna</div>
  <div class="abs btn btn--red" style="left:277px;top:935px;width:80px">VIEW ALL</div>

  <div class="abs" style="left:360px;top:1000px;width:274px;height:120px;background:radial-gradient(ellipse at 70% 30%,rgba(221,178,120,.45),rgba(255,255,255,0) 70%)" role="img" aria-label="Soft caramel popcorn backdrop"></div>
  <div class="abs photo" style="left:58px;top:1046px;width:252px;height:152px;background:linear-gradient(135deg,#3b4a5c,#8b6c52 50%,#2f3744)" role="img" aria-label="Promo video: gift packages for family, friends and clients">
    <svg class="abs" style="left:14px;top:12px" width="30" height="30"><circle cx="15" cy="15" r="14" fill="#b3202a" opacity=".85"/><path d="M12 10L20 15L12 20Z" fill="#fff"/></svg>
  </div>
  <svg class="abs sec-icon" style="left:336px;top:1042px" viewBox="0 0 12 14"><circle cx="6" cy="4" r="4" fill="#8cc63f"/><path d="M6 8V13M3 13H9" stroke="#999"/><circle cx="7" cy="1.5" r="1.5" fill="#e0202a"/></svg>
  <div class="abs h2" style="left:334px;top:1066px">GET YOUR <b>SNACK ON!</b></div>
  <div class="abs para" style="left:336px;top:1092px;width:226px">Lorem ipsum dolor sit amet, consectetur adipiscing elit, sed do eiusmod tempor incididunt ut labore et dolore magna aliqua. Ut enim ad minim veniam, quis nostrud exercitation ullamco laboris nisi ut aliquip ex ea commodo consequat. Duis aute irure dolor in reprehenderit in voluptate velit esse cillum dolore eu fugiat nulla pariatur.</div>

  <div class="abs recipe"></div>
  <div class="abs" style="left:350px;top:1250px;width:260px;height:200px;background:radial-gradient(ellipse at 40% 55%,#6b3d1c,#a86a35 30%,#f2dd8b 55%,rgba(233,100,100,0) 72%)" role="img" aria-label="Chocolate cupcake with butter and mint leaves"></div>
  <svg class="abs sec-icon" style="left:60px;top:1272px" viewBox="0 0 12 14"><circle cx="6" cy="4" r="4" fill="#8cc63f"/><path d="M6 8V13M3 13H9" stroke="#fff"/><circle cx="7" cy="1.5" r="1.5" fill="#fff"/></svg>
  <div class="abs h2" style="left:58px;top:1297px;color:#fff;font-weight:600">SPECIAL RECIPE</div>
  <div class="abs para" style="left:59px;top:1323px;width:262px">Lorem ipsum dolor sit amet, consectetur adipiscing elit, sed do eiusmod tempor incididunt ut labore et dolore magna aliqua. Ut enim ad minim veniam, quis nostrud exercitation ullamco laboris nisi ut aliquip ex ea commodo consequat.</div>
  <div class="abs btn btn--green" style="left:58px;top:1387px;width:82px">VIEW DETAILS</div>
  <div class="abs dots" style="left:611px;top:1305px"><span></span><span></span><span></span><span></span><span></span></div>

  <svg class="abs sec-icon" style="left:311px;top:1490px" viewBox="0 0 12 14"><circle cx="6" cy="4" r="4" fill="#8cc63f"/><path d="M6 8V13M3 13H9" stroke="#999"/><circle cx="7" cy="1.5" r="1.5" fill="#e0202a"/></svg>
  <div class="abs h2" style="left:0;top:1514px;width:634px;text-align:center">OUR <b>TESTIMONIALS</b></div>
  <div class="abs" style="left:101px;top:1530px;font-size:22px;color:#888;font-family:Georgia,serif">“</div>
  <div class="abs" style="left:505px;top:1594px;font-size:22px;color:#888;font-family:Georgia,serif">”</div>
  <div class="abs arrow" style="left:42px;top:1560px">‹</div>
  <div class="abs arrow" style="left:580px;top:1560px">›</div>
  <div class="abs" style="left:110px;top:1555px;width:414px;text-align:center;font-size:6.8px;line-height:13.5px;font-style:italic;color:#666">Lorem ipsum dolor sit amet, consectetur adipiscing elit, sed do eiusmod tempor incididunt ut labore et dolore magna aliqua. Ut enim ad minim veniam, quis nostrud exercitation ullamco laboris nisi ut aliquip ex ea commodo consequat. Duis aute irure dolor in reprehenderit in voluptate velit esse cillum dolore eu fugiat nulla pariatur.</div>
  <div class="abs" style="left:0;top:1600px;width:634px;text-align:center;font-size:10px;font-style:italic;font-weight:600">- John Dood</div>
  <div class="abs stars" style="left:0;top:1616px;width:634px">★★★★★</div>

  <div class="abs" style="left:0;top:1685px;width:634px;text-align:center;font-family:Montserrat,sans-serif;font-weight:700;font-size:17px">OUR EVENTS</div>
  <div class="abs photo" style="left:58px;top:1715px;width:160px;height:105px;background:linear-gradient(135deg,#6e9a2c,#c83a24 45%,#e3b12a)" role="img" aria-label="Colourful popcorn mix"></div>
  <div class="abs photo" style="left:237px;top:1715px;width:160px;height:105px;background:linear-gradient(135deg,#5d7fa3,#efe6c8 45%,#c79a52)" role="img" aria-label="Vanilla ice cream scoop with nuts"></div>
  <div class="abs photo" style="left:416px;top:1715px;width:160px;height:105px;background:linear-gradient(135deg,#9c7a68,#4a2c1e 50%,#b39784)" role="img" aria-label="Chocolate dipped ice cream cone against brick"></div>
  <div class="abs event-date" style="left:61px;top:1839px">FEB<b>05</b></div>
  <div class="abs event-date" style="left:239px;top:1839px">FEB<b>05</b></div>
  <div class="abs event-date" style="left:418px;top:1839px">FEB<b>05</b></div>
  <div class="abs event-title" style="left:97px;top:1841px">Lorem ipsumotmet<br>consectetur iisin.</div>
  <div class="abs event-title" style="left:276px;top:1841px">Lorem ipsumotmet<br>consectetur iisin.</div>
  <div class="abs event-title" style="left:455px;top:1841px">Lorem ipsumotmet<br>consectetur iisin.</div>
  <div class="abs event-meta" style="left:61px;top:1880px">by <span style="color:#e0202a">●</span> John Doe</div>
  <div class="abs event-meta" style="left:239px;top:1880px">by <span style="color:#e0202a">●</span> John Doe</div>
  <div class="abs event-meta" style="left:418px;top:1880px">by <span style="color:#e0202a">●</span> John Doe</div>
  <div class="abs event-text" style="left:61px;top:1890px">Lorem ipsum dolor sit amet,rdiscing elit, seo eiusmod tempocnt ut labore et dolore malid minim veniam,uis nostrud exre</div>
  <div class="abs event-text" style="left:239px;top:1890px">Lorem ipsum dolor sit amet,rdiscing elit, seo eiusmod tempocnt ut labore et dolore malid minim veniam,uis nostrud exre</div>
  <div class="abs event-text" style="left:418px;top:1890px">Lorem ipsum dolor sit amet,rdiscing elit, seo eiusmod tempocnt ut labore et dolore malid minim veniam,uis nostrud exre</div>

  <svg class="abs footer" viewBox="0 0 634 292"><path d="M0 50 Q330 100 634 0 L634 292 L0 292Z" fill="#000"/><path d="M0 50 Q200 92 370 78" fill="none" stroke="#8cc63f" stroke-width="5"/></svg>
  <div class="abs foot-h" style="left:60px;top:2022px">GET IN TOUCH</div>
  <div class="abs foot-h" style="left:246px;top:2022px">INFORMATION</div>
  <div class="abs foot-h" style="left:369px;top:2022px">CONTACT US</div>
  <div class="abs foot-ico" style="left:60px;top:2045px"></div>
  <div class="abs foot-t" style="left:82px;top:2045px">220 Maple Grove Ave #14,<br>Cedar Bend TX 70123,</div>
  <div class="abs foot-ico" style="left:60px;top:2090px"></div>
  <div class="abs foot-t" style="left:82px;top:2090px">+1 (555) 014-2290</div>
  <div class="abs foot-ico" style="left:60px;top:2118px"></div>
  <div class="abs foot-t" style="left:82px;top:2119px">rt@fizzlane.net</div>
  <ul class="abs foot-links" style="left:246px;top:2044px"><li>Home Page</li><li>About us</li><li>Menu</li><li>Gift/Promotion</li><li>Contact us</li></ul>
  <div class="abs field" style="left:369px;top:2045px;width:101px;height:16px">Name</div>
  <div class="abs field" style="left:474px;top:2045px;width:101px;height:16px">Email Address</div>
  <div class="abs field" style="left:369px;top:2067px;width:206px;height:43px">Message</div>
  <div class="abs btn btn--green" style="left:369px;top:2116px;width:77px;line-height:16px;font-size:6px">SUBMIT MESSAGE</div>
  <div class="abs" style="left:60px;top:2145px;width:515px;height:1px;background:#555"></div>
  <div class="abs foot-t" style="left:0;top:2157px;width:634px;text-align:center;font-size:7px">© Copyrights 2019 Fizz Lane | All Rights Reserved</div>
</div>

<!-- ===== HOME PAGE WITH COUPON MODAL ===== -->
<div class="page page--popup">
  <div class="abs topbar"><span>☏ Call us Today : (555) 014-2290</span><span>✉ Email Address : hello@fizzlane.net</span></div>
  <div class="abs header"></div>
  <div class="abs brand"><i></i>FIZZ LANE</div>
  <div class="abs search">Search<b></b></div>
  <div class="abs lang">Eng ▾</div><div class="abs flag"></div>
  <div class="abs social"><span></span><span></span><span></span><span></span></div>
  <div class="abs burger"><span></span><span></span><span></span></div>

  <div class="abs hero"></div>
  <div class="abs hero-photo" role="img" aria-label="Two glass mugs of whipped-cream shake and caramel popcorn"></div>
  <div class="abs hero-title">FIZZ LANE</div>
  <div class="abs hero-sub">OREM IPSUM DOLOR SIT AMET,<br>CONSECTETUR ADIPISCING ELIT, SED DO</div>
  <div class="abs hero-offer">30% OFFER</div>
  <div class="abs btn btn--green" style="left:58px;top:262px;width:82px">GET STARTED</div>
  <div class="abs dots" style="left:603px;top:170px"><span></span><span></span><span></span><span></span><span></span></div>
  <svg class="abs" style="left:0;top:320px" width="634" height="70" viewBox="0 0 634 70"><path d="M0 60 Q300 -10 634 50 L634 70 L0 70Z" fill="#fff"/><path d="M150 22 Q420 0 634 50" fill="none" stroke="#6fae25" stroke-width="4"/></svg>

  <svg class="abs sec-icon" style="left:97px;top:412px" viewBox="0 0 12 14"><circle cx="6" cy="4" r="4" fill="#8cc63f"/><path d="M6 8V13M3 13H9" stroke="#999"/><circle cx="7" cy="1.5" r="1.5" fill="#e0202a"/></svg>
  <div class="abs h2" style="left:58px;top:436px">FEATURED <b>DISHES</b></div>
  <div class="abs para" style="left:59px;top:462px;width:242px">Lorem ipsum dolor sit amet, consectetur adipiscing elit, sed do eiusmod tempor incididunt ut labore et dolore magna aliqua. Ut enim ad minim veniam, quis nostrud exercitation ullamco laboris nisi ut aliquip ex ea commodo consequat. Duis aute irure dolor in reprehenderit in voluptate velit esse cillum dolore eu fugiat nulla pariatur. Excepteur sint occaecat cupidatat non proident,</div>
  <div class="abs count" style="left:58px;top:554px"><div>08<small>DAYS</small></div><div>20<small>HRS</small></div><div>10<small>MIN</small></div><div>45<small>SEC</small></div></div>
  <div class="abs photo" style="left:384px;top:422px;width:192px;height:160px;background:radial-gradient(circle,#e6e4e2,#bdbab7 60%,#efefef)" role="img" aria-label="Cookies and cream ice cream with chocolate cookies"></div>
  <div class="abs photo" style="left:332px;top:536px;width:92px;height:64px;background:linear-gradient(135deg,#8a6a4d,#d9d2c4 50%,#6d5441)" role="img" aria-label="Bowl of ice cream on a wooden table"></div>

  <div class="abs menu-bg"></div>
  <svg class="abs sec-icon" style="left:311px;top:670px" viewBox="0 0 12 14"><circle cx="6" cy="4" r="4" fill="#8cc63f"/><path d="M6 8V13M3 13H9" stroke="#999"/><circle cx="7" cy="1.5" r="1.5" fill="#e0202a"/></svg>
  <div class="abs h2" style="left:0;top:693px;width:634px;text-align:center">OUR MENU</div>
  <div class="abs card-img" style="left:74px;top:729px"><div style="background:linear-gradient(180deg,#fff 30%,#c9d86b 60%,#b64d79)" role="img" aria-label="Colourful gourmet popcorn in a green cup"></div></div>
  <div class="abs card-img" style="left:246px;top:729px"><div style="background:radial-gradient(ellipse at 50% 45%,#8a5b3c,#d9c6b7 35%,#fff 60%)" role="img" aria-label="Ice cream sundae with a cherry"></div></div>
  <div class="abs card-img" style="left:418px;top:729px"><div style="background:radial-gradient(ellipse at 50% 45%,#8e1b25,#c46a70 35%,#fff 60%)" role="img" aria-label="Red boozy shake in a glass mug"></div></div>
  <div class="abs sale" style="left:195px;top:715px">Sale!</div>
  <div class="abs card-title" style="left:74px;top:861px">POPCORN</div>
  <div class="abs card-title" style="left:246px;top:861px">ICE CREAM</div>
  <div class="abs card-title" style="left:418px;top:861px">BOOZY SHAKE</div>
  <div class="abs stars" style="left:74px;top:874px;width:139px">★★★★★</div>
  <div class="abs stars" style="left:246px;top:874px;width:139px">★★★★★</div>
  <div class="abs stars" style="left:418px;top:874px;width:139px">★★★★★</div>
  <div class="abs card-text" style="left:69px;top:887px">Lorem ipsum dolor sit amet, consectetur adipiscing elit, sed do eiusmod tempor incididunt ut labore et dolore magna</div>
  <div class="abs card-text" style="left:241px;top:887px">Lorem ipsum dolor sit amet, consectetur adipiscing elit, sed do eiusmod tempor incididunt ut labore et dolore magna</div>
  <div class="abs card-text" style="left:413px;top:887px">Lorem ipsum dolor sit amet, consectetur adipiscing elit, sed do eiusmod tempor incididunt ut labore et dolore magna</div>
  <div class="abs btn btn--red" style="left:277px;top:935px;width:80px">VIEW ALL</div>

  <div class="abs" style="left:360px;top:1000px;width:274px;height:120px;background:radial-gradient(ellipse at 70% 30%,rgba(221,178,120,.45),rgba(255,255,255,0) 70%)" role="img" aria-label="Soft caramel popcorn backdrop"></div>
  <div class="abs photo" style="left:58px;top:1046px;width:252px;height:152px;background:linear-gradient(135deg,#3b4a5c,#8b6c52 50%,#2f3744)" role="img" aria-label="Promo video: gift packages for family, friends and clients">
    <svg class="abs" style="left:14px;top:12px" width="30" height="30"><circle cx="15" cy="15" r="14" fill="#b3202a" opacity=".85"/><path d="M12 10L20 15L12 20Z" fill="#fff"/></svg>
  </div>
  <svg class="abs sec-icon" style="left:336px;top:1042px" viewBox="0 0 12 14"><circle cx="6" cy="4" r="4" fill="#8cc63f"/><path d="M6 8V13M3 13H9" stroke="#999"/><circle cx="7" cy="1.5" r="1.5" fill="#e0202a"/></svg>
  <div class="abs h2" style="left:334px;top:1066px">GET YOUR <b>SNACK ON!</b></div>
  <div class="abs para" style="left:336px;top:1092px;width:226px">Lorem ipsum dolor sit amet, consectetur adipiscing elit, sed do eiusmod tempor incididunt ut labore et dolore magna aliqua. Ut enim ad minim veniam, quis nostrud exercitation ullamco laboris nisi ut aliquip ex ea commodo consequat. Duis aute irure dolor in reprehenderit in voluptate velit esse cillum dolore eu fugiat nulla pariatur.</div>

  <div class="abs recipe"></div>
  <div class="abs" style="left:350px;top:1250px;width:260px;height:200px;background:radial-gradient(ellipse at 40% 55%,#6b3d1c,#a86a35 30%,#f2dd8b 55%,rgba(233,100,100,0) 72%)" role="img" aria-label="Chocolate cupcake with butter and mint leaves"></div>
  <svg class="abs sec-icon" style="left:60px;top:1272px" viewBox="0 0 12 14"><circle cx="6" cy="4" r="4" fill="#8cc63f"/><path d="M6 8V13M3 13H9" stroke="#fff"/><circle cx="7" cy="1.5" r="1.5" fill="#fff"/></svg>
  <div class="abs h2" style="left:58px;top:1297px;color:#fff;font-weight:600">SPECIAL RECIPE</div>
  <div class="abs para" style="left:59px;top:1323px;width:262px">Lorem ipsum dolor sit amet, consectetur adipiscing elit, sed do eiusmod tempor incididunt ut labore et dolore magna aliqua. Ut enim ad minim veniam, quis nostrud exercitation ullamco laboris nisi ut aliquip ex ea commodo consequat.</div>
  <div class="abs btn btn--green" style="left:58px;top:1387px;width:82px">VIEW DETAILS</div>
  <div class="abs dots" style="left:611px;top:1305px"><span></span><span></span><span></span><span></span><span></span></div>

  <svg class="abs sec-icon" style="left:311px;top:1490px" viewBox="0 0 12 14"><circle cx="6" cy="4" r="4" fill="#8cc63f"/><path d="M6 8V13M3 13H9" stroke="#999"/><circle cx="7" cy="1.5" r="1.5" fill="#e0202a"/></svg>
  <div class="abs h2" style="left:0;top:1514px;width:634px;text-align:center">OUR <b>TESTIMONIALS</b></div>
  <div class="abs" style="left:101px;top:1530px;font-size:22px;color:#888;font-family:Georgia,serif">“</div>
  <div class="abs" style="left:505px;top:1594px;font-size:22px;color:#888;font-family:Georgia,serif">”</div>
  <div class="abs arrow" style="left:42px;top:1560px">‹</div>
  <div class="abs arrow" style="left:580px;top:1560px">›</div>
  <div class="abs" style="left:110px;top:1555px;width:414px;text-align:center;font-size:6.8px;line-height:13.5px;font-style:italic;color:#666">Lorem ipsum dolor sit amet, consectetur adipiscing elit, sed do eiusmod tempor incididunt ut labore et dolore magna aliqua. Ut enim ad minim veniam, quis nostrud exercitation ullamco laboris nisi ut aliquip ex ea commodo consequat. Duis aute irure dolor in reprehenderit in voluptate velit esse cillum dolore eu fugiat nulla pariatur.</div>
  <div class="abs" style="left:0;top:1600px;width:634px;text-align:center;font-size:10px;font-style:italic;font-weight:600">- John Dood</div>
  <div class="abs stars" style="left:0;top:1616px;width:634px">★★★★★</div>

  <div class="abs" style="left:0;top:1685px;width:634px;text-align:center;font-family:Montserrat,sans-serif;font-weight:700;font-size:17px">OUR EVENTS</div>
  <div class="abs photo" style="left:58px;top:1715px;width:160px;height:105px;background:linear-gradient(135deg,#6e9a2c,#c83a24 45%,#e3b12a)" role="img" aria-label="Colourful popcorn mix"></div>
  <div class="abs photo" style="left:237px;top:1715px;width:160px;height:105px;background:linear-gradient(135deg,#5d7fa3,#efe6c8 45%,#c79a52)" role="img" aria-label="Vanilla ice cream scoop with nuts"></div>
  <div class="abs photo" style="left:416px;top:1715px;width:160px;height:105px;background:linear-gradient(135deg,#9c7a68,#4a2c1e 50%,#b39784)" role="img" aria-label="Chocolate dipped ice cream cone against brick"></div>
  <div class="abs event-date" style="left:61px;top:1839px">FEB<b>05</b></div>
  <div class="abs event-date" style="left:239px;top:1839px">FEB<b>05</b></div>
  <div class="abs event-date" style="left:418px;top:1839px">FEB<b>05</b></div>
  <div class="abs event-title" style="left:97px;top:1841px">Lorem ipsumotmet<br>consectetur iisin.</div>
  <div class="abs event-title" style="left:276px;top:1841px">Lorem ipsumotmet<br>consectetur iisin.</div>
  <div class="abs event-title" style="left:455px;top:1841px">Lorem ipsumotmet<br>consectetur iisin.</div>
  <div class="abs event-meta" style="left:61px;top:1880px">by <span style="color:#e0202a">●</span> John Doe</div>
  <div class="abs event-meta" style="left:239px;top:1880px">by <span style="color:#e0202a">●</span> John Doe</div>
  <div class="abs event-meta" style="left:418px;top:1880px">by <span style="color:#e0202a">●</span> John Doe</div>
  <div class="abs event-text" style="left:61px;top:1890px">Lorem ipsum dolor sit amet,rdiscing elit, seo eiusmod tempocnt ut labore et dolore malid minim veniam,uis nostrud exre</div>
  <div class="abs event-text" style="left:239px;top:1890px">Lorem ipsum dolor sit amet,rdiscing elit, seo eiusmod tempocnt ut labore et dolore malid minim veniam,uis nostrud exre</div>
  <div class="abs event-text" style="left:418px;top:1890px">Lorem ipsum dolor sit amet,rdiscing elit, seo eiusmod tempocnt ut labore et dolore malid minim veniam,uis nostrud exre</div>

  <svg class="abs footer" viewBox="0 0 634 292"><path d="M0 50 Q330 100 634 0 L634 292 L0 292Z" fill="#000"/><path d="M0 50 Q200 92 370 78" fill="none" stroke="#8cc63f" stroke-width="5"/></svg>
  <div class="abs foot-h" style="left:60px;top:2022px">GET IN TOUCH</div>
  <div class="abs foot-h" style="left:246px;top:2022px">INFORMATION</div>
  <div class="abs foot-h" style="left:369px;top:2022px">CONTACT US</div>
  <div class="abs foot-ico" style="left:60px;top:2045px"></div>
  <div class="abs foot-t" style="left:82px;top:2045px">220 Maple Grove Ave #14,<br>Cedar Bend TX 70123,</div>
  <div class="abs foot-ico" style="left:60px;top:2090px"></div>
  <div class="abs foot-t" style="left:82px;top:2090px">+1 (555) 014-2290</div>
  <div class="abs foot-ico" style="left:60px;top:2118px"></div>
  <div class="abs foot-t" style="left:82px;top:2119px">rt@fizzlane.net</div>
  <ul class="abs foot-links" style="left:246px;top:2044px"><li>Home Page</li><li>About us</li><li>Menu</li><li>Gift/Promotion</li><li>Contact us</li></ul>
  <div class="abs field" style="left:369px;top:2045px;width:101px;height:16px">Name</div>
  <div class="abs field" style="left:474px;top:2045px;width:101px;height:16px">Email Address</div>
  <div class="abs field" style="left:369px;top:2067px;width:206px;height:43px">Message</div>
  <div class="abs btn btn--green" style="left:369px;top:2116px;width:77px;line-height:16px;font-size:6px">SUBMIT MESSAGE</div>
  <div class="abs" style="left:60px;top:2145px;width:515px;height:1px;background:#555"></div>
  <div class="abs foot-t" style="left:0;top:2157px;width:634px;text-align:center;font-size:7px">© Copyrights 2019 Fizz Lane | All Rights Reserved</div>

  <div class="abs overlay"></div>
  <div class="abs modal">
    <div class="abs modal-brand">FIZZ LANE</div>
    <div class="abs modal-h">Save 10% on the Next Order of Your Favorite Snacks!</div>
    <div class="abs modal-p">orem ipsum dolor sit amet, consectetur adipiscing elit, sed do eiusmod tempor incididunt ut labore et dolore</div>
    <div class="abs modal-input">Email Address*</div>
    <div class="abs btn btn--red modal-btn">GET MY COUPON</div>
  </div>
  <div class="abs close"><svg width="40" height="40"><path d="M14 14L26 26M26 14L14 26" stroke="#222" stroke-width="3.5" stroke-linecap="round"/></svg></div>
</div>

</body>
</html>
```